Property development & Investment company Need a logo & business card design

Our name is KT Estates Australia Pty Ltd
Need logo & business card design

Target Market(s)

People dealing in commercial property

Industry/Entity Type

Business

Contact Information for Business Card

KT Estates Australia
Peter Dunmore Mobile0419 703 646
Email Peter@quillbarrow.com.au

Font styles to use
Sans Serif

Requirements
Must have
• company name
• contact details
Nice to have
• KT Estates Bold
• Australia Not Bold
Should not have
• To busy of a look

```html
<!DOCTYPE html>
<html lang="en">
<head>
<meta charset="utf-8">
<title>KT Estates Australia – Business Card</title>
<link rel="stylesheet" href="https://fonts.googleapis.com/css2?family=Questrial&family=Roboto+Slab:wght@400&display=swap">
<style>
  :root {
    --page-bg: #ececec;
    --card-bg: #fbfbfb;
    --brand-blue: #0f4fa8;
    --brand-blue-soft: #5f8ccc;
    --text-grey: #5c5c5c;
    --card-edge: #dcdcdc;
  }
  * { box-sizing: border-box; margin: 0; padding: 0; }
  html, body {
    width: 1200px;
    height: 1200px;
    overflow: hidden;
    background: var(--page-bg);
  }
  .canvas {
    position: relative;
    width: 1200px;
    height: 1200px;
  }
  .business-card {
    position: absolute;
    left: 220px;
    top: 218px;
    width: 784px;
    height: 450px;
    background: var(--card-bg);
    border: 1px solid var(--card-edge);
    overflow: hidden;
  }
  .card-accent {
    position: absolute;
    top: 0;
    right: 0;
    width: 390px;
    height: 100%;
    background: linear-gradient(100deg, var(--card-bg) 0%, var(--brand-blue-soft) 60%, var(--brand-blue) 100%);
  }
  .brand-lockup {
    position: absolute;
    display: flex;
    align-items: center;
    gap: 14px;
  }
  .brand-square {
    width: 22px;
    height: 22px;
    background: var(--brand-blue);
    flex: none;
  }
  .brand-name {
    font-family: "Roboto Slab", serif;
    font-weight: 400;
    color: var(--brand-blue);
    line-height: 1.05;
  }
  .brand-name .line { display: block; }
  .card-brand { left: 70px; top: 178px; }
  .card-brand .brand-name { font-size: 28px; }
  .card-brand .brand-name .line-sub { font-size: 19px; }
  .contact-name {
    position: absolute;
    left: 70px;
    top: 288px;
    font-family: "Questrial", sans-serif;
    font-size: 25px;
    color: var(--text-grey);
  }
  .contact-list {
    position: absolute;
    left: 72px;
    top: 354px;
    list-style: none;
    font-family: "Questrial", sans-serif;
    font-size: 20px;
    color: var(--text-grey);
  }
  .contact-list li {
    display: flex;
    align-items: center;
    gap: 9px;
    height: 31px;
  }
  .contact-icon {
    width: 16px;
    height: 16px;
    fill: none;
    stroke: var(--text-grey);
    stroke-width: 1.6;
  }
  .logo-brand {
    left: 50%;
    top: 962px;
    transform: translateX(-50%);
  }
  .logo-brand .brand-name { font-size: 32px; text-align: center; }
  .logo-brand .brand-name .line-sub { font-size: 22px; }
</style>
</head>
<body>
<main class="canvas">
  <section class="business-card">
    <div class="card-accent" role="img" aria-label="Decorative brand accent area in blue tones"></div>

    <div class="brand-lockup card-brand">
      <span class="brand-square"></span>
      <p class="brand-name">
        <span class="line">KT Estates</span>
        <span class="line line-sub">Australia Pty Ltd</span>
      </p>
    </div>

    <p class="contact-name">Peter Dunmore</p>

    <ul class="contact-list">
      <li>
        <svg class="contact-icon" viewBox="0 0 16 16" aria-hidden="true">
          <rect x="4" y="1.5" width="8" height="13" rx="1.5"/>
          <line x1="6.5" y1="12" x2="9.5" y2="12"/>
        </svg>
        <span>0438 512 907</span>
      </li>
      <li>
        <svg class="contact-icon" viewBox="0 0 16 16" aria-hidden="true">
          <rect x="1.5" y="3.5" width="13" height="9"/>
          <polyline points="1.5,3.5 8,9 14.5,3.5"/>
        </svg>
        <span>Peter@quillbarrow.com.au</span>
      </li>
    </ul>
  </section>

  <div class="brand-lockup logo-brand">
    <span class="brand-square"></span>
    <p class="brand-name">
      <span class="line">KT Estates</span>
      <span class="line line-sub">Australia Pty Ltd</span>
    </p>
  </div>
</main>
</body>
</html>
```